Fretwise Riff Hall WebSite

I am looking for a website design for FretwiseRiffHall.com. If you are unfamiliar with the term "guitar lick": a guitar lick is a simple piece of music that is used in an improvisation or solo. All of the famous guitarists that you probably have heard of (Tobin Marlowe, Dale Pemberly, etc.) have their own set of unique licks. This is what defines their style. The "Dojo" in the site name refers to a karate dojo. Basically, like a person would master karate in a karate dojo, a guitarist can master guitar licks in the Fretwise Riff Hall. The purpose of FretwiseRiffHall is to show users very high quality videos (vidstreamo) and music notation for a variety of licks. Many of the guitar licks on the site will be from famous guitarists. There will also be licks that are not from famous guitarists, that are just general licks in a particular style or genre.

Target Market(s)

Intermediate and above guitar players.

Industry/Entity Type

Vidstreamo

Requirements
Must have
• 1) The look and feel of the site must be based on the logo that I have attached. First and foremost, this site must be FUN. The page should fit with the mood of the logo. The logo should be incorporated well into the header design. It would be nice to see the logo theme used throughout the same page in some creative and reasonable way.
• 2) There will be three main navigation tabs on the home page: Licks, JamTracks, and Blog. The Licks section will be broken into Licks by Artist, and licks by genre (eg. Jazz, Rock, Blues, Fusion, Heavy Metal, Country, etc.)
• 3) There needs to be 3 main sections on the Home Page: Lick of the Day, Recently Added Licks, and Featured Licks. These 3 sections must contain thumbnails of the videos, along with a text description.
Nice to have
• Use the character from the logo or the karate theme in some creative way on the page.

```html
<!DOCTYPE html>
<html lang="en">
<head>
<meta charset="utf-8">
<title>Fretwise Riff Hall</title>
<link href="https://fonts.googleapis.com/css2?family=Open+Sans:wght@400;600;700&display=swap" rel="stylesheet">
<style>
:root{
  --red:#e8112d;
  --blue:#1b86c4;
  --blue-dark:#1a5276;
  --ink:#333333;
  --muted:#666666;
  --grey-bar:#5c5c5c;
  --panel:#f0f0f0;
  --black:#0a0a0a;
  --white:#ffffff;
}
*{box-sizing:border-box;margin:0;padding:0}
html,body{width:699px;height:1200px;overflow:hidden;background:var(--white)}
body{position:relative;font-family:"Open Sans",Arial,sans-serif;color:var(--ink)}
.abs{position:absolute}

/* header */
.brand{left:26px;top:14px;display:flex;align-items:center;gap:7px}
.brand-mark{width:40px;height:40px;border-radius:50%;background:var(--blue)}
.brand-name{font-size:12px;font-weight:700;color:var(--ink)}
.util-links{right:37px;top:6px;font-size:8px;color:var(--muted);display:flex;gap:9px}
.util-links .active{color:var(--blue)}
.main-nav{top:34px;left:388px;display:flex;gap:6px}
.main-nav a{display:block;width:65px;height:23px;line-height:23px;text-align:center;font-size:9.5px;font-weight:600;color:var(--white);background:#1b1b1b;text-decoration:none;border-top:2px solid #444}
.main-nav a.current{background:var(--red);border-top-color:#ff5a6b}

/* hero */
.hero{left:0;top:62px;width:699px;height:329px;background:radial-gradient(ellipse at 68% 55%,#3a2d24 0%,#1a1614 35%,#080808 75%)}
.hero-photo{position:absolute;left:318px;top:0;width:381px;height:329px;background:radial-gradient(ellipse at 45% 60%,#5a3a22 0%,#2a1d16 40%,rgba(10,10,10,0) 75%)}
.hero-title{left:62px;top:194px;font-size:17px;font-weight:700;color:var(--white)}
.hero-text{left:62px;top:221px;width:230px;font-size:9px;line-height:14px;color:#e6e6e6}
.hero-arrow{top:218px}

/* welcome */
.section-title{font-size:17px;font-weight:400;color:#333}
.welcome-photo{left:34px;top:458px;width:105px;height:96px;background:linear-gradient(135deg,#7a5a3c,#3a2a1e)}
.welcome-text{left:147px;top:455px;width:318px;font-size:7.4px;line-height:10.8px;color:var(--muted)}
.btn{height:14px;line-height:14px;font-size:7.5px;color:var(--white);text-align:center}
.btn-red{background:var(--red)}
.btn-blue{background:var(--blue)}

/* featured grid */
.tile{width:133px;height:83px}
.caption{width:133px;text-align:center;font-size:9.5px;color:var(--muted)}
.caption.hot{color:var(--red)}

/* join */
.join{left:35px;top:870px;width:427px;height:79px;background:var(--blue);box-shadow:0 1px 2px rgba(0,0,0,.35)}
.join-title{left:27px;top:27px;font-size:15px;color:var(--white)}
.join-input{left:129px;top:30px;width:170px;height:22px;background:var(--white);font-size:7.5px;color:#555;padding:6px 8px}
.join-btn{left:309px;top:30px;width:94px;height:22px;background:var(--blue-dark);color:var(--white);font-size:9px;line-height:22px;text-align:center}

/* sidebar */
.sidebar{left:490px;top:414px;width:174px;height:607px;background:var(--white);border:4px solid var(--panel)}
.side-head{left:495px;width:164px;height:27px;background:var(--grey-bar);color:var(--white);font-size:11px;line-height:27px;padding-left:11px}
.lick{left:506px;display:flex;gap:12px}
.lick-thumb{width:42px;height:42px;position:relative}
.lick-meta{font-size:7.5px;line-height:12px;color:#333}
.lick-meta strong{font-size:8.5px;font-weight:600;display:block;margin-bottom:1px}
.view-all{left:613px;font-size:7.5px;color:var(--red)}
.play{position:absolute}
.blog-photo{left:506px;top:888px;width:144px;height:56px;background:linear-gradient(90deg,#1a1a1a,#4a2020 50%,#151515)}
.blog-title{left:507px;top:950px;font-size:8.5px;font-weight:600}
.blog-date{left:506px;top:963px;font-size:7.5px;display:flex;gap:13px}
.blog-text{left:508px;top:977px;width:141px;font-size:6px;line-height:8.5px;color:var(--muted);text-align:justify}

/* footer */
.cta{left:0;top:1048px;width:699px;height:53px;background:var(--red)}
.cta-title{left:170px;top:11px;font-size:22px;font-weight:700;color:var(--white)}
.cta-btn{left:424px;top:12px;width:81px;height:26px;background:#1d1d1d;color:var(--white);font-size:7.5px;font-weight:600;text-align:center;line-height:26px}
.footer{left:0;top:1101px;width:699px;height:99px;background:var(--black)}
.foot-links{left:0;top:19px;width:699px;text-align:center;font-size:8px;color:#999;word-spacing:2px}
.foot-rule{left:0;top:55px;width:699px;height:1px;background:#2a2a2a}
.copyright{left:17px;top:73px;font-size:7px;color:#aaa}
.socials{left:512px;top:66px}
</style>
</head>
<body>

<header>
  <div class="abs brand"><span class="brand-mark"></span><span class="brand-name">FretwiseRiffHall</span></div>
  <div class="abs util-links"><span class="active">Login</span><span>|</span><span>Register</span><span>|</span><span>Contact</span></div>
  <nav class="abs main-nav"><a class="current">Home</a><a>Licks</a><a>Jamtracks</a><a>Blog</a></nav>
</header>

<section class="abs hero">
  <div class="hero-photo" role="img" aria-label="Guitarist in a black hat playing a sunburst electric guitar"></div>
  <div class="abs hero-title">Lorem ipsum dolor sit</div>
  <p class="abs hero-text">Lorem Ipsum is simply dummy text of the printing and typesetting industry.</p>
  <svg class="abs hero-arrow" style="left:18px" width="10" height="16"><path d="M8 1 L2 8 L8 15" fill="none" stroke="#888" stroke-width="1.3"/></svg>
  <svg class="abs hero-arrow" style="left:671px" width="10" height="16"><path d="M2 1 L8 8 L2 15" fill="none" stroke="#888" stroke-width="1.3"/></svg>
</section>

<main>
  <h2 class="abs section-title" style="left:35px;top:423px">Welcome To Our Site</h2>
  <div class="abs welcome-photo" role="img" aria-label="Close-up of fingers on guitar strings"></div>
  <p class="abs welcome-text">It is a long established fact that a reader will be distracted by the readable content of a page when looking at its layout. The point of using Lorem Ipsum is that it has a more-or-less normal distribution of letters, as opposed to using 'Content here, content here', making it look like readable English. Many desktop publishing packages and web page editors now use Lorem Ipsum as their default model text, and a search for 'lorem ipsum' will uncover many web sites still in their infancy.</p>
  <div class="abs btn btn-red" style="left:148px;top:540px;width:66px">Read More</div>
  <div class="abs btn btn-blue" style="left:219px;top:540px;width:65px">Join Now</div>

  <h2 class="abs section-title" style="left:33px;top:580px">Featured Pages</h2>
  <div class="abs tile" style="left:35px;top:618px;background:linear-gradient(180deg,#e8e8e8,#8a4a4a 60%,#333)" role="img" aria-label="Rock band posing with guitars"></div>
  <svg class="abs" style="left:92px;top:650px" width="20" height="20"><circle cx="10" cy="10" r="9" fill="#c4162a"/><path d="M8 6 L14 10 L8 14Z" fill="#fff"/></svg>
  <div class="abs tile" style="left:184px;top:618px;background:linear-gradient(135deg,#2a1a10,#8a6040 55%,#1a120c)" role="img" aria-label="Hand on an electric guitar neck"></div>
  <div class="abs tile" style="left:331px;top:618px;background:linear-gradient(180deg,#0a0806,#b06020 65%,#3a1a08)" role="img" aria-label="Guitar strings over a lit soundhole"></div>
  <div class="abs tile" style="left:35px;top:737px;background:linear-gradient(135deg,#6a4a30,#c89a70 50%,#8a5a3a)" role="img" aria-label="Acoustic guitar body seen up close"></div>
  <div class="abs tile" style="left:184px;top:737px;background:linear-gradient(135deg,#2a1005,#d06010 50%,#f0b020)" role="img" aria-label="Bass guitar played in front of flames"></div>
  <div class="abs tile" style="left:331px;top:737px;background:linear-gradient(90deg,#6a5038,#a08060 50%,#5a4030)" role="img" aria-label="Acoustic guitar leaning on a wooden wall"></div>
  <div class="abs caption hot" style="left:35px;top:707px">Lorem ipsum dolor</div>
  <div class="abs caption" style="left:184px;top:707px">Lorem ipsum dolor</div>
  <div class="abs caption" style="left:331px;top:707px">Lorem ipsum dolor</div>
  <div class="abs caption" style="left:35px;top:826px">Lorem ipsum dolor</div>
  <div class="abs caption" style="left:184px;top:826px">Lorem ipsum dolor</div>
  <div class="abs caption" style="left:331px;top:826px">Lorem ipsum dolor</div>

  <section class="abs join">
    <div class="abs join-title">Join With Us</div>
    <div class="abs join-input">Email Id</div>
    <div class="abs join-btn">SUBSRIBE</div>
  </section>
</main>

<aside>
  <div class="abs sidebar"></div>
  <div class="abs side-head" style="top:418px">Recently Added Licks</div>
  <div class="abs lick" style="top:453px"><div class="lick-thumb" style="background:linear-gradient(135deg,#1a1a1a,#d08030)" role="img" aria-label="Acoustic guitar video thumbnail"><svg class="play" style="left:11px;top:11px" width="20" height="20"><circle cx="10" cy="10" r="9" fill="#c4162a"/><path d="M8 6 L14 10 L8 14Z" fill="#fff"/></svg></div><div class="lick-meta"><strong>Lorem ipsum sit</strong>12-05-2015<br>Jhon doe</div></div>
  <div class="abs lick" style="top:507px"><div class="lick-thumb" style="background:linear-gradient(135deg,#e8d8b0,#9a7040)" role="img" aria-label="Acoustic guitar soundhole thumbnail"></div><div class="lick-meta"><strong>Lorem ipsum sit</strong>12-05-2015<br>Jhon doe</div></div>
  <div class="abs lick" style="top:561px"><div class="lick-thumb" style="background:linear-gradient(135deg,#f0e8e0,#8a5a30)" role="img" aria-label="Street guitarist thumbnail"></div><div class="lick-meta"><strong>Lorem ipsum sit</strong>12-05-2015<br>Jhon doe</div></div>
  <div class="abs view-all" style="top:607px">View all &#9656;</div>

  <div class="abs side-head" style="top:637px">Most Popular Licks</div>
  <div class="abs lick" style="top:671px"><div class="lick-thumb" style="background:linear-gradient(135deg,#1a1a1a,#d08030)" role="img" aria-label="Acoustic guitar video thumbnail"><svg class="play" style="left:11px;top:11px" width="20" height="20"><circle cx="10" cy="10" r="9" fill="#c4162a"/><path d="M8 6 L14 10 L8 14Z" fill="#fff"/></svg></div><div class="lick-meta"><strong>Lorem ipsum sit</strong>12-05-2015<br>Jhon doe</div></div>
  <div class="abs lick" style="top:725px"><div class="lick-thumb" style="background:linear-gradient(135deg,#111,#777)" role="img" aria-label="Hands on guitar fretboard thumbnail"></div><div class="lick-meta"><strong>Lorem ipsum sit</strong>12-05-2015<br>Jhon doe</div></div>
  <div class="abs lick" style="top:779px"><div class="lick-thumb" style="background:linear-gradient(135deg,#222,#aaa)" role="img" aria-label="Black and white fretboard close-up thumbnail"></div><div class="lick-meta"><strong>Lorem ipsum sit</strong>12-05-2015<br>Jhon doe</div></div>
  <div class="abs view-all" style="top:825px">View all &#9656;</div>

  <div class="abs side-head" style="top:854px">Blog Entry of the Week</div>
  <div class="abs blog-photo" role="img" aria-label="Player with a red electric guitar"></div>
  <svg class="abs" style="left:568px;top:906px" width="20" height="20"><circle cx="10" cy="10" r="9" fill="#c4162a"/><path d="M8 6 L14 10 L8 14Z" fill="#fff"/></svg>
  <div class="abs blog-title">Lorem ipsum sit</div>
  <div class="abs blog-date"><span>12-05-2015</span><span>Jhon doe</span></div>
  <p class="abs blog-text">Lorem Ipsum has been the industry's standard dummy text ever since the 1500s, when an unknown printer</p>
</aside>

<section class="abs cta">
  <div class="abs cta-title">Want to Know more?</div>
  <div class="abs cta-btn">JOIN WITH US</div>
</section>

<footer class="abs footer">
  <div class="abs foot-links">Home &nbsp;|&nbsp; Licks &nbsp;|&nbsp; Jamtracks &nbsp;|&nbsp; Blog</div>
  <div class="abs foot-rule"></div>
  <svg class="abs" style="left:343px;top:52px" width="12" height="12"><rect width="12" height="12" fill="#0a0a0a"/><path d="M2 6 L6 2 L10 6 M2 10 L6 6 L10 10" fill="none" stroke="#aaa" stroke-width="1.2"/></svg>
  <div class="abs copyright">copyrights &copy; 2015 yoursite All rights reserved</div>
  <svg class="abs socials" width="135" height="26">
    <g fill="none" stroke="#bbb" stroke-width="1">
      <rect x="4" y="4" width="14" height="14" transform="rotate(45 11 11)"/>
      <rect x="26" y="4" width="14" height="14" transform="rotate(45 33 11)"/>
      <rect x="48" y="4" width="14" height="14" transform="rotate(45 55 11)" fill="#fff"/>
      <rect x="70" y="4" width="14" height="14" transform="rotate(45 77 11)"/>
      <rect x="92" y="4" width="14" height="14" transform="rotate(45 99 11)"/>
      <rect x="114" y="4" width="14" height="14" transform="rotate(45 121 11)"/>
    </g>
  </svg>
</footer>

</body>
</html>
```